Premium Audio and HD Video with AFS!

AFS is a mobile studio that provides premium audio and HD video recording for the classical and jazz community in the Boston area. Specializing in concerts, recitals, auditions, studio releases, lectures, podcasts and more.
My website:
http://amberfieldsoundworks.example
https://www.facebook.com/AFSoundworks/
Target Market(s)
classical and jazz instrumentalists, vocalists, ensembles, choruses, a cappella groups, podcasters
Industry/Entity Type
Audio
Font styles to use
Serif
Colors
Designer to choose colors to be used in the design.
Requirements
Must have
- My logo!
- Must convey that this mobile recording studio is for classical and jazz musicians... not rock bands etc.
- I provide event recording as well as "studio recording" (for CDs etc)
- Eye catching
- Must be scalable for different size flyers... full page, half page etc
- I will use it for bulletin boards.. so the front side is most important... if the design is two sided, the lesser important info should be on the back side.
Nice to have
- Use some of the photos on my facebook page? Not sure they are high res or decent photos..
- https://www.facebook.com/AFSoundworks/
Should not have
- Anything depicting a rock band or similar

```html
<!DOCTYPE html>
<html lang="en">
<head>
<meta charset="utf-8">
<title>Amberfield Soundworks Poster</title>
<link rel="stylesheet" href="https://fonts.googleapis.com/css2?family=Montserrat:wght@400;500;600;700&display=swap">
<style>
  :root {
    --page-bg: #e9e9e7;
    --navy-deep: #12073f;
    --navy: #1a1470;
    --royal: #1d3fb8;
    --cyan-glow: #3fc4ff;
    --text-light: #ffffff;
    --text-soft: #dfe4ff;
    --photo-light: #b8b8bc;
    --photo-dark: #6d6d72;
  }
  * { box-sizing: border-box; margin: 0; padding: 0; }
  html, body { width: 1200px; height: 1200px; overflow: hidden; }
  body {
    background: var(--page-bg);
    font-family: "Montserrat", sans-serif;
    color: var(--text-light);
  }
  .poster {
    position: absolute;
    left: 200px; top: 30px;
    width: 800px; height: 1140px;
    overflow: hidden;
    background:
      radial-gradient(circle at 88% 8%, rgba(230,200,255,.55) 0 45px, transparent 70px),
      radial-gradient(circle at 22% 10%, rgba(80,170,255,.45) 0 50px, transparent 90px),
      radial-gradient(circle at 8% 2%, rgba(170,210,255,.6) 0 18px, transparent 30px),
      radial-gradient(circle at 15% 55%, rgba(120,90,200,.35) 0 70px, transparent 110px),
      radial-gradient(circle at 85% 52%, rgba(120,90,200,.3) 0 70px, transparent 110px),
      radial-gradient(ellipse at 50% 30%, var(--royal) 0%, var(--navy) 55%, var(--navy-deep) 85%);
  }
  .poster__kicker {
    position: absolute; top: 80px; width: 100%;
    text-align: center; font-size: 13px; font-weight: 500;
    letter-spacing: .45em; color: var(--text-soft);
  }
  .poster__photo {
    position: absolute; left: 155px; top: 140px;
    width: 490px; height: 490px; border-radius: 50%;
    background: radial-gradient(circle at 45% 35%, var(--photo-light), var(--photo-dark));
    border: 5px solid #e8f6ff;
    box-shadow: 0 0 18px 6px var(--cyan-glow), 0 0 60px 10px rgba(63,196,255,.35);
  }
  .services__title {
    position: absolute; top: 695px; width: 100%;
    text-align: center; font-size: 17px; font-weight: 700;
    letter-spacing: .3em;
  }
  .services__grid {
    position: absolute; top: 738px; left: 80px; width: 640px;
    list-style: none;
    display: grid; grid-template-columns: repeat(3, 1fr); gap: 12px 14px;
  }
  .services__item {
    border: 1px solid rgba(255,255,255,.8);
    height: 58px; display: flex; align-items: center; justify-content: center;
    font-size: 16px; font-weight: 500; letter-spacing: .02em;
  }
  .audience {
    position: absolute; top: 888px; width: 100%; text-align: center;
  }
  .audience__title { font-size: 18px; font-weight: 700; margin-bottom: 8px; }
  .audience__list { font-size: 14px; line-height: 1.5; color: var(--text-soft); }
  .footer {
    position: absolute; left: 0; bottom: 0; width: 100%; height: 140px;
    border-top: 1px solid rgba(255,255,255,.7);
    background: radial-gradient(ellipse at 50% 40%, #23338c, var(--navy-deep) 70%);
    display: flex; justify-content: space-between; align-items: center;
    padding: 0 45px;
  }
  .footer__contact-person {
    align-self: flex-end; margin-bottom: 34px;
    font-size: 11px; font-weight: 700; line-height: 1.4;
  }
  .footer__brand {
    font-size: 19px; font-weight: 600; color: var(--text-soft);
    letter-spacing: .03em; white-space: nowrap; margin-left: 40px;
  }
  .footer__brand-mark {
    display: inline-block; width: 11px; height: 11px; border-radius: 50%;
    background: var(--text-soft); margin-right: 9px; vertical-align: middle;
  }
  .footer__details {
    align-self: flex-start; margin-top: 30px; text-align: right;
    font-size: 9.5px; font-weight: 700; line-height: 1.5; white-space: nowrap;
  }
</style>
</head>
<body>
  <main class="poster">
    <p class="poster__kicker">AMBERFIELD PROVIDES</p>
    <div class="poster__photo" role="img" aria-label="Photo of a singer in headphones performing at a studio microphone"></div>

    <h2 class="services__title">AUDIO AND VIDEO PRODUCTION SERVICES FOR</h2>
    <ul class="services__grid">
      <li class="services__item">CONCERTS</li>
      <li class="services__item">RECITALS</li>
      <li class="services__item">STUDIO RELEASES</li>
      <li class="services__item">AUDITIONS</li>
      <li class="services__item">LECTURES</li>
      <li class="services__item">PODCASTS &amp; MORE</li>
    </ul>

    <section class="audience">
      <h3 class="audience__title">SERVING THE</h3>
      <p class="audience__list">Solo Vocal/Instrumental | Chamber Music | Choral<br>Orchestral | and Contemporary Acappella | Communities</p>
    </section>

    <footer class="footer">
      <p class="footer__contact-person">DANIEL REYES<br>PRINCIPAL ENGINEER</p>
      <p class="footer__brand"><span class="footer__brand-mark"></span>Amberfield Soundworks</p>
      <p class="footer__details">555.014.2273<br>DAN@AMBERFIELDSOUNDWORKS.EXAMPLE<br>AMBERFIELDSOUNDWORKS.EXAMPLE</p>
    </footer>
  </main>
</body>
</html>
```